PlumVerse Business Cards

I need a business card designed for PlumVerse. To get an idea of what we do please visit https://brisklayout.example/para-artistas-7

```html
<!DOCTYPE html>
<html lang="en">
<head>
<meta charset="utf-8">
<title>PlumVerse Business Cards</title>
<link rel="stylesheet" href="https://fonts.googleapis.com/css2?family=Montserrat:wght@300;400&family=Source+Sans+3:wght@400;700&display=swap">
<style>
  :root {
    --backdrop: #e3e3e3;
    --card-dark: #1b1f24;
    --card-light: #f4f4f4;
    --accent: #e08f1e;
    --text-light: #ffffff;
    --text-dark: #1b1f24;
    --deco-light: #f3ebe1;
    --deco-dark: #2c3036;
  }
  * { margin: 0; padding: 0; box-sizing: border-box; }
  html, body { width: 1200px; height: 960px; overflow: hidden; }
  body {
    background: var(--backdrop);
    position: relative;
    font-family: "Source Sans 3", "Source Sans Pro", sans-serif;
  }
  .card {
    position: absolute;
    left: 291px;
    width: 609px;
    height: 349px;
    overflow: hidden;
  }
  .card--front { top: 104px; background: var(--card-dark); }
  .card--back { top: 506px; background: var(--card-dark); }

  .front-decoration {
    position: absolute;
    left: 392px; top: 0;
    width: 217px; height: 349px;
    background: linear-gradient(160deg, var(--deco-dark) 0%, var(--card-dark) 75%);
  }
  .front-wordmark {
    position: absolute;
    left: 51px; top: 256px;
    font-family: "Montserrat", sans-serif;
    font-weight: 300;
    font-size: 38px;
    letter-spacing: 0.2em;
    text-transform: uppercase;
    color: var(--text-light);
  }

  .back-shape { position: absolute; inset: 0; }
  .back-brand {
    position: absolute;
    left: 48px; top: 155px;
    display: flex;
    align-items: center;
    gap: 22px;
  }
  .brand-dot {
    width: 40px; height: 40px;
    border: 2px solid var(--accent);
    border-radius: 50%;
  }
  .back-wordmark {
    font-family: "Montserrat", sans-serif;
    font-weight: 400;
    font-size: 22px;
    letter-spacing: 0.18em;
    text-transform: uppercase;
    color: var(--text-dark);
  }

  .contact {
    position: absolute;
    left: 365px; top: 87px;
    color: var(--text-light);
    font-size: 15px;
    line-height: 21px;
  }
  .contact__name { color: var(--accent); font-weight: 700; font-size: 19px; line-height: 24px; }
  .contact__role { margin-bottom: 18px; }
  .contact__address { margin-bottom: 7px; }
  .contact__line { display: flex; align-items: center; gap: 5px; }
  .contact__line svg { width: 14px; height: 14px; flex: none; }
</style>
</head>
<body>
  <section class="card card--front">
    <div class="front-decoration" role="img" aria-label="Large faint decorative brand graphic"></div>
    <div class="front-wordmark">PlumVerse</div>
  </section>

  <section class="card card--back">
    <svg class="back-shape" width="609" height="349" viewBox="0 0 609 349">
      <polygon points="0,0 244,0 342,174 244,349 0,349" fill="var(--accent)"/>
      <polygon points="0,0 229,0 328,174 229,349 0,349" fill="var(--card-light)"/>
    </svg>
    <div class="back-brand">
      <span class="brand-dot"></span>
      <span class="back-wordmark">PlumVerse</span>
    </div>
    <div class="contact">
      <div class="contact__name">Daniel Reyes</div>
      <div class="contact__role">Owner</div>
      <div class="contact__address">48 Harbor Lane<br>Coral Bay, Florida, 33000</div>
      <div class="contact__line">
        <svg viewBox="0 0 16 16"><path d="M4 1.5l2.2 3-1.4 1.6a8 8 0 0 0 5 5l1.6-1.4 3 2.2-1.4 2.6C7.5 14.5 1.5 8.5 1.4 3z" fill="var(--accent)"/></svg>
        (555) 010-2468
      </div>
      <div class="contact__line">
        <svg viewBox="0 0 16 16"><rect x="1" y="3" width="14" height="10" fill="none" stroke="var(--accent)" stroke-width="1.6"/><path d="M1 3.5l7 5.5 7-5.5" fill="none" stroke="var(--accent)" stroke-width="1.6"/></svg>
        daniel@plumverse.example
      </div>
      <div class="contact__line">
        <svg viewBox="0 0 16 16"><circle cx="8" cy="8" r="6.5" fill="none" stroke="var(--accent)" stroke-width="1.4"/><ellipse cx="8" cy="8" rx="3" ry="6.5" fill="none" stroke="var(--accent)" stroke-width="1.2"/><path d="M1.5 8h13" stroke="var(--accent)" stroke-width="1.2"/></svg>
        www.plumverse.example
      </div>
    </div>
  </section>
</body>
</html>
```